We are a doctors medical practice
I need the business card to be eye catching and memorable,
to reflect professionalism, yet also warmth and care

the numbers need to be easy to see, for the elderly

and the logo also in a location that is large enough to see and be eye catching

Back of card:
opening hours:
Mon- Fri 8.30am to 6pm
Sat 9am to 4pm

rows for appontments, date and time
Updates

HiĀ 

Modification to company name

BRAMBLEWOOD HOME HEALTH MEDICAL PRACTICE

Thanks
Clara

Reason: I am look for a unique design that also fulfils the design brief

I have attempted to post a .eps and .ai file of the logo

Target Market(s)

needs to appeal to the majority, mainly adults

Industry/Entity Type

Medical

Contact Information for Business Card

company name: Bramblewood Home Health Medical Practice
Name: Dr Clara Ostrowski-Vey
Qualifications: MBBS, Bsci(med), FRACGP, DCH, SH&FPA, Dip Derm
Address: Shop 3/41-43 Calder Rd, Brookvale 2371
Ph: 02 9418 3052
Fax: 02 9436 8120

Requirements
Nice to have
• I like balance
gold/ silver incorporated, as well as the other colours in the logo- but not limited to these colours
a "medical" feel
Should not have
• dark or strong colours

```html
<!DOCTYPE html>
<html lang="en">
<head>
<meta charset="utf-8">
<title>Bramblewood Home Health Medical Practice – Business Card</title>
<link rel="stylesheet" href="https://fonts.googleapis.com/css2?family=Open+Sans:wght@400;600;800&family=Kalam:wght@700&display=swap">
<style>
  :root {
    --olive: #8a9a2c;
    --olive-dark: #6f7d1f;
    --gold: #d8c22e;
    --gold-light: #e4d24a;
    --white: #ffffff;
    --ink: #1f2410;
    --sky: #3c86c8;
    --page: #eceae4;
  }
  * { box-sizing: border-box; margin: 0; padding: 0; }
  html, body { width: 1200px; height: 720px; overflow: hidden; background: var(--page); }
  body { position: relative; font-family: "Open Sans", sans-serif; }

  .card {
    position: absolute;
    top: 40px;
    width: 390px;
    height: 640px;
    overflow: hidden;
    box-shadow: 0 8px 24px rgba(0,0,0,.18);
  }
  .card--back { left: 170px; background: var(--gold); }
  .card--front { left: 640px; background: var(--olive); }
  .card__shapes { position: absolute; inset: 0; width: 100%; height: 100%; }

  .brand-mark { position: absolute; display: flex; align-items: center; gap: 10px; }
  .brand-mark__dot { width: 34px; height: 34px; border-radius: 50%; background: var(--sky); flex: none; }
  .brand-mark__name { font-weight: 800; font-size: 17px; letter-spacing: .5px; }

  /* back */
  .card--back .brand-mark { top: 220px; left: 50%; transform: translateX(-50%); }
  .card--back .brand-mark__name { color: var(--olive-dark); }
  .practice-name {
    font-weight: 800; text-transform: uppercase; line-height: 1.15;
  }
  .card--back .practice-name {
    position: absolute; top: 280px; left: 30px; right: 30px;
    text-align: center; color: var(--olive-dark); font-size: 22px;
  }
  .hours { position: absolute; top: 395px; left: 34px; color: var(--ink); font-size: 17px; line-height: 1.35; }
  .hours__title { color: var(--sky); font-weight: 600; }

  /* front */
  .card--front .brand-mark { top: 48px; left: 32px; }
  .card--front .brand-mark__name { color: var(--olive-dark); }
  .doctor { position: absolute; top: 118px; left: 32px; right: 24px; color: var(--white); }
  .doctor__name { font-family: "Kalam", cursive; font-size: 24px; line-height: 1.1; }
  .doctor__quals { font-size: 13px; margin-top: 6px; line-height: 1.35; }
  .card--front .practice-name {
    position: absolute; top: 232px; left: 32px; right: 24px; color: var(--white); font-size: 21px;
  }
  .contact { position: absolute; top: 318px; left: 32px; color: var(--white); font-size: 16px; line-height: 1.45; font-weight: 600; }
  .stethoscope {
    position: absolute; left: 170px; top: 420px; width: 200px; height: 150px;
    border-radius: 40px;
    background: radial-gradient(ellipse at 50% 55%, rgba(34,84,96,.75), rgba(34,84,96,.15) 70%, transparent 75%);
  }
</style>
</head>
<body>

<section class="card card--back">
  <svg class="card__shapes" viewBox="0 0 390 640" aria-hidden="true">
    <path d="M0 0 H390 V60 Q210 95 0 190 Z" fill="var(--olive)"/>
    <path d="M0 205 Q210 110 390 75" fill="none" stroke="var(--white)" stroke-width="10"/>
    <path d="M0 640 V585 Q200 470 390 455 V640 Z" fill="var(--olive)"/>
    <path d="M0 565 Q200 455 390 438" fill="none" stroke="var(--white)" stroke-width="10"/>
  </svg>
  <div class="brand-mark">
    <span class="brand-mark__dot"></span>
    <span class="brand-mark__name">Bramblewood</span>
  </div>
  <h1 class="practice-name">Bramblewood Home Health Medical Practice</h1>
  <div class="hours">
    <p class="hours__title">Opening Hours:</p>
    <p>Mon- Fri 8.30am to 6pm</p>
    <p>Sat 9am to 4pm</p>
  </div>
</section>

<section class="card card--front">
  <svg class="card__shapes" viewBox="0 0 390 640" aria-hidden="true">
    <path d="M140 0 H390 V95 Q290 30 140 0 Z" fill="var(--gold)"/>
    <path d="M0 38 Q240 20 390 110" fill="none" stroke="var(--white)" stroke-width="9"/>
    <path d="M0 640 V590 Q180 520 390 575 V640 Z" fill="var(--gold)"/>
    <path d="M0 572 Q190 500 390 555" fill="none" stroke="var(--white)" stroke-width="9"/>
  </svg>
  <div class="brand-mark">
    <span class="brand-mark__dot"></span>
    <span class="brand-mark__name">Bramblewood</span>
  </div>
  <div class="doctor">
    <p class="doctor__name">Dr Clara Ostrowski-Vey</p>
    <p class="doctor__quals">MBBS, Bsci(med), FRACGP, DCH,<br>SH&amp;FPA, Dip Derm</p>
  </div>
  <h2 class="practice-name">Bramblewood Home Health Medical Practice</h2>
  <address class="contact" style="font-style:normal">
    <p>Shop 3/41-43 Calder Rd,</p>
    <p>Brookvale 2371</p>
    <p>tel : 02 9418 3052</p>
    <p>fax : 02 9436 8120</p>
  </address>
  <div class="stethoscope" role="img" aria-label="Stethoscope illustration"></div>
</section>

</body>
</html>
```